Dental 2 practice oudoor signs

I need 2 high quality practice signs designed
sign 1 ( 1.6m high by 0.8m wide)
sign 2 ( sign 1.05m high by 0.80m wide)

I had sign 1 displayed before which i have attached but it doest look as professional now. We are a multi award winning dental clinic. Both signs will be printed on dibond and be at a 45 degree to each other so that the person walking past will only see one sign, unless he walks in the opposite direction. Here is the brief of sign 1 and sign 2 but feel free to diverse away from the brief and do something differet

Sign 1
Merlow Dental, Implant & Orthodontic Centre

Size of sign 1600 Height by 800 WIde
website: www.merlowdentalsurgery.example
Sign text

Multi-Award Winning
Centre of Excellence

Dental Implants from £ 38.23/mo
Clearfitra Braces from £ 29.23/mo
Dental Veneers from £11.13/mo
Smile Makeovers from £34.13/mo
Specialist Orthodontics from £29.23/mo
Facial Aesthetics from £22.16/mo

020 7395 0618
www.merlowdentalsurgery.example

Each of the above treatements should be also represented graphically so the sign is very colorful and draws your attention but gives a quality feel about it
You can find graphics wherever you need to, to advertise the services

Sign 2.
Use any detail you wish from sign 1 but i definately want
Multi-Award Winning on both signs

Target Market(s)

Passers by who are driving past dental practice or pedestrians who are walking past practice

Industry/Entity Type

Dental Clinic

Colors

Designer to choose colors to be used in the design.

Requirements
Must have
• See brief

```html
<!DOCTYPE html>
<html lang="en">
<head>
<meta charset="utf-8">
<title>Merlow Dental – Practice Signs</title>
<link href="https://fonts.googleapis.com/css2?family=Lato:wght@400;700;900&family=Open+Sans:wght@400;600&display=swap" rel="stylesheet">
<style>
  :root{
    --navy:#2c3a6f;
    --blue:#2aa3dc;
    --sky:#cfe9f7;
    --yellow:#f7ec1e;
    --price:#f4e63a;
    --white:#ffffff;
    --canvas:#e4e4e4;
    --dot:#f7ec1e;
  }
  *{box-sizing:border-box;margin:0;padding:0}
  html,body{width:1200px;height:746px;overflow:hidden;background:var(--canvas)}
  .board{position:relative;width:1200px;height:746px}
  .sign{position:absolute;top:23px;width:350px;height:700px;overflow:hidden;background:var(--white);box-shadow:0 4px 14px rgba(0,0,0,.25)}
  .sign--classic{left:205px}
  .sign--banner{left:645px}
  .layer{position:absolute;left:0;top:0;width:100%;height:100%}
  .brand{position:absolute;display:flex;flex-direction:column;align-items:center;justify-content:center;background:var(--white);border:4px solid var(--navy);border-radius:50%;font-family:'Lato',sans-serif;font-weight:700;color:var(--navy);text-align:center;letter-spacing:1px}
  .sign--classic .brand{left:6px;top:6px;width:112px;height:112px;font-size:13px;line-height:1.25}
  .sign--banner .brand{left:105px;top:-20px;width:140px;height:110px;border-radius:0 0 70px 70px;border-top:none;font-size:14px;padding-top:18px;line-height:1.25}
  .award-seal{position:absolute;left:212px;top:196px;width:134px;height:134px;border-radius:50%;background:var(--white);border:4px solid var(--navy);padding:22px 0 0 20px;font-family:'Lato',sans-serif;line-height:1}
  .award-seal__title{display:block;font-weight:900;font-size:24px;color:var(--navy)}
  .award-seal__sub{display:block;font-weight:700;font-size:13px;color:var(--blue);margin-top:3px;line-height:1.05}
  .prices{position:absolute;list-style:none;font-family:'Open Sans',sans-serif;color:var(--white)}
  .prices li{display:flex;justify-content:space-between;align-items:baseline}
  .prices .name{position:relative;padding-left:14px}
  .prices .name::before{content:"";position:absolute;left:0;top:50%;width:7px;height:7px;margin-top:-3px;border-radius:50%;background:var(--dot)}
  .prices .price{font-weight:600;color:var(--price)}
  .prices .price small{font-size:.65em}
  .sign--classic .prices{left:10px;right:12px;top:466px;font-size:13.5px}
  .sign--classic .prices li{height:20px}
  .sign--banner .prices{left:14px;right:14px;top:372px;font-size:13.5px}
  .sign--banner .prices li{height:33px}
  .phone{position:absolute;left:0;right:0;top:590px;height:48px;background:var(--yellow);color:var(--navy);font-family:'Lato',sans-serif;font-weight:900;font-size:26px;display:flex;align-items:center;justify-content:center}
  .web{position:absolute;left:0;right:0;top:638px;height:62px;background:var(--navy);color:var(--white);font-family:'Open Sans',sans-serif;font-weight:600;font-size:14px;letter-spacing:1.2px;display:flex;align-items:center;justify-content:center}
</style>
</head>
<body>
<main class="board">

  <!-- Sign 1: classic layout -->
  <section class="sign sign--classic" aria-label="Merlow Dental practice sign, circle layout">
    <svg class="layer" viewBox="0 0 350 700">
      <defs>
        <linearGradient id="lowerBlue" x1="0" y1="0" x2="0" y2="1">
          <stop offset="0" stop-color="#4cb6e6"/>
          <stop offset="1" stop-color="#1f98d6"/>
        </linearGradient>
      </defs>
      <rect role="img" aria-label="Photo of a smiling child at a dental check-up" x="0" y="0" width="350" height="300" fill="#e9eef2"/>
      <rect x="0" y="300" width="350" height="290" fill="url(#lowerBlue)"/>
      <ellipse role="img" aria-label="Photo of a smiling couple" cx="125" cy="372" rx="150" ry="80" fill="#dfe6ea" stroke="var(--navy)" stroke-width="5"/>
    </svg>
    <div class="brand">MERLOW<br>DENTAL</div>
    <div class="award-seal">
      <span class="award-seal__title">MULTI<br>AWARD</span>
      <span class="award-seal__sub">Winning<br>Centre of<br>Excellence</span>
    </div>
    <ul class="prices">
      <li><span class="name">Dental Implants from</span><span class="price">£38.23/<small>mo</small></span></li>
      <li><span class="name">Clearfitra Braces from</span><span class="price">£29.23/<small>mo</small></span></li>
      <li><span class="name">Dental Veneers from</span><span class="price">£11.13/<small>mo</small></span></li>
      <li><span class="name">Smile Makeovers from</span><span class="price">£34.13/<small>mo</small></span></li>
      <li><span class="name">Specialist Orthodontics from</span><span class="price">£29.23/<small>mo</small></span></li>
      <li><span class="name">Facial Aesthetics from</span><span class="price">£22.16/<small>mo</small></span></li>
    </ul>
    <div class="phone">020 7395 0618</div>
    <div class="web">www.merlowdentalsurgery.example</div>
  </section>

  <!-- Sign 2: banner layout -->
  <section class="sign sign--banner" aria-label="Merlow Dental practice sign, banner layout">
    <svg class="layer" viewBox="0 0 350 700">
      <rect x="0" y="0" width="350" height="590" fill="var(--navy)"/>
      <rect role="img" aria-label="Photo of a smiling child holding a dental mirror" x="0" y="0" width="350" height="300" fill="#e6edf1"/>
      <path d="M0 262 Q175 330 350 262 L350 340 Q175 400 0 340 Z" fill="var(--white)"/>
      <path id="awardArc" d="M20 300 Q175 352 330 290" fill="none"/>
      <path id="subArc" d="M16 322 Q175 374 336 308" fill="none"/>
      <text font-family="Lato, sans-serif" font-weight="900" font-size="27" fill="var(--navy)">
        <textPath href="#awardArc" startOffset="50%" text-anchor="middle">MULTI-AWARD</textPath>
      </text>
      <text font-family="Lato, sans-serif" font-weight="700" font-size="12.5" fill="var(--blue)" letter-spacing="0.6">
        <textPath href="#subArc" startOffset="50%" text-anchor="middle">WINNING CENTRE OF EXCELLENCE</textPath>
      </text>
    </svg>
    <div class="brand">MERLOW<br>DENTAL</div>
    <ul class="prices">
      <li><span class="name">Dental Implants from</span><span class="price">£38.23/<small>mo</small></span></li>
      <li><span class="name">Clearfitra Braces from</span><span class="price">£29.23/<small>mo</small></span></li>
      <li><span class="name">Dental Veneers from</span><span class="price">£11.13/<small>mo</small></span></li>
      <li><span class="name">Smile Makeovers from</span><span class="price">£34.13/<small>mo</small></span></li>
      <li><span class="name">Specialist Orthodontics from</span><span class="price">£29.23/<small>mo</small></span></li>
      <li><span class="name">Facial Aesthetics from</span><span class="price">£22.16/<small>mo</small></span></li>
    </ul>
    <div class="phone">020 7395 0618</div>
    <div class="web">www.merlowdentalsurgery.example</div>
  </section>

</main>
</body>
</html>
```